KV Taxidermy

I need business Cards with my logo and a background photo of one of my taxidermy mounts.
I would like a black back drop behind it all and what ever looks best for my contact information (red or white?)
Marcus Pellow
555-218-4907
kvtaxidermy512@mailvex.net
Chatterly page

```html
<!DOCTYPE html>
<html lang="en">
<head>
<meta charset="utf-8">
<title>KV Taxidermy – Business Card</title>
<link rel="stylesheet" href="https://fonts.googleapis.com/css2?family=Montserrat:wght@300;400;600&display=swap">
<style>
  :root {
    --page-bg: #d9d9d9;
    --card-dark: #1d2022;
    --card-mid: #2e3336;
    --accent: #c98a54;
    --text-light: #e6e6e6;
    --text-soft: #cfcfcf;
    --mount-light: #e9e7e2;
    --mount-rock: #6f7780;
  }
  * { margin: 0; padding: 0; box-sizing: border-box; }
  html, body {
    width: 1200px; height: 900px; overflow: hidden;
    background: var(--page-bg);
    font-family: "Montserrat", sans-serif;
  }
  .canvas {
    width: 1200px; height: 900px;
    display: flex; align-items: center; justify-content: center;
  }
  .business-card {
    position: relative;
    width: 1050px; height: 600px;
    background: radial-gradient(ellipse at 40% 20%, var(--card-mid) 0%, var(--card-dark) 75%);
    border-radius: 6px;
    overflow: hidden;
    box-shadow: 0 12px 30px rgba(0,0,0,0.35);
  }
  .brand-mark {
    position: absolute; left: 80px; top: 120px;
    display: flex; align-items: center; gap: 14px;
    color: var(--text-light);
    font-size: 30px; font-weight: 600; letter-spacing: 1px;
  }
  .brand-mark .brand-square {
    width: 26px; height: 26px; background: var(--text-light);
  }
  .holder {
    position: absolute; left: 545px; top: 58px;
  }
  .holder-name {
    color: var(--accent); font-size: 36px; font-weight: 600;
  }
  .holder-title {
    color: var(--text-light); font-size: 28px; font-weight: 300; margin-top: 2px;
  }
  .mount-photo {
    position: absolute; left: 430px; top: 160px;
    width: 590px; height: 400px;
    background:
      radial-gradient(ellipse 45% 32% at 52% 32%, var(--mount-light) 0%, rgba(233,231,226,0.85) 60%, transparent 100%),
      radial-gradient(ellipse 55% 38% at 70% 72%, var(--mount-rock) 0%, rgba(111,119,128,0.6) 60%, transparent 100%);
  }
  .address {
    position: absolute; left: 80px; top: 320px;
    color: var(--text-soft); font-size: 21px; line-height: 1.6; font-weight: 400;
  }
  .contact-list {
    position: absolute; left: 80px; top: 420px;
    list-style: none;
    color: var(--text-soft); font-size: 21px;
  }
  .contact-list li {
    display: flex; align-items: center; gap: 18px; height: 40px;
  }
  .contact-icon { width: 20px; height: 20px; flex: none; }
  .social-square { width: 18px; height: 18px; background: var(--accent); flex: none; margin: 0 1px; }
</style>
</head>
<body>
<main class="canvas">
  <section class="business-card">
    <div class="brand-mark"><span class="brand-square"></span>KV Taxidermy</div>

    <header class="holder">
      <h1 class="holder-name">Marcus Pellow</h1>
      <p class="holder-title">Taxidermist</p>
    </header>

    <div class="mount-photo" role="img" aria-label="Photo of a white Dall sheep ram mount lying on a grey rock base"></div>

    <p class="address">Marcus Pellow, Box 48117<br>Ridgeford, YT, Y0B 2K4</p>

    <ul class="contact-list">
      <li>
        <svg class="contact-icon" viewBox="0 0 24 24" aria-hidden="true"><path fill="var(--accent)" d="M6.6 10.8a15 15 0 0 0 6.6 6.6l2.2-2.2a1 1 0 0 1 1-.25 11.4 11.4 0 0 0 3.6.57 1 1 0 0 1 1 1V20a1 1 0 0 1-1 1A17 17 0 0 1 3 4a1 1 0 0 1 1-1h3.5a1 1 0 0 1 1 1c0 1.25.2 2.45.57 3.6a1 1 0 0 1-.25 1z"/></svg>
        555-218-4907
      </li>
      <li>
        <svg class="contact-icon" viewBox="0 0 24 24" aria-hidden="true"><rect x="2" y="5" width="20" height="14" fill="none" stroke="var(--accent)" stroke-width="2"/><path d="M2 5l10 8 10-8" fill="none" stroke="var(--accent)" stroke-width="2"/></svg>
        kvtaxidermy512@mailvex.net
      </li>
      <li>
        <span class="social-square" aria-label="Chatterly"></span>
        KV Taxidermy
      </li>
    </ul>
  </section>
</main>
</body>
</html>
```